" Somos um eccomerce de iluminação led. temos um portfólio muito vasto de produtos para atender diversas demandas: consumidor final, revenda, condomínios e empresas no modo geral. "

```html
<!DOCTYPE html>
<html lang="pt-BR">
<head>
<meta charset="utf-8">
<title>Catálogo Luminárias LED 2018</title>
<link rel="stylesheet" href="https://fonts.googleapis.com/css2?family=Open+Sans:wght@400;600;700&display=swap">
<style>
  :root{
    --bg:#e6e6e6;
    --page:#ffffff;
    --red:#b31f27;
    --ink:#3b3b3b;
    --muted:#6b6b6b;
    --row:#efefef;
    --row-alt:#f7f7f7;
    --icon:#4a4a4a;
  }
  *{box-sizing:border-box;margin:0;padding:0}
  html,body{width:1200px;height:1200px;overflow:hidden;background:var(--bg);font-family:"Open Sans",Arial,sans-serif;color:var(--ink)}
  .spread{position:absolute;left:40px;top:182px;width:1120px;height:836px;display:flex;box-shadow:0 10px 30px rgba(0,0,0,.18)}
  .page{position:relative;width:560px;height:836px;background:var(--page);overflow:hidden}
  .page--left{box-shadow:inset -14px 0 18px -14px rgba(0,0,0,.18)}
  .page--right{box-shadow:inset 14px 0 18px -14px rgba(0,0,0,.18)}
  .banner{position:absolute;left:0;top:0;width:100%;height:120px;
    background:linear-gradient(180deg,#cfd2d6 0%,#e1e3e6 45%,#ffffff 100%)}
  .side-band{position:absolute;top:0;width:26px;height:836px;background:var(--red);}
  .side-band span{position:absolute;left:50%;top:50%;transform:translate(-50%,-50%) rotate(-90deg);white-space:nowrap;color:#fff;font-size:10px;font-weight:600;letter-spacing:.2px}
  .page--left .side-band{right:14px}
  .page--right .side-band{right:4px}
  .spine-strip{position:absolute;left:10px;top:0;width:14px;height:300px;background:var(--red)}
  .page-number{position:absolute;bottom:22px;font-size:11px;color:var(--muted)}
  .page--left .page-number{left:22px}
  .page--right .page-number{left:44px}

  .product{position:absolute;width:470px}
  .page--left .product{left:40px}
  .page--right .product{left:52px}
  .product__head{display:flex;align-items:center;height:34px}
  .product__title{font-size:25px;font-weight:600;color:var(--ink);letter-spacing:-.3px}
  .product__tag{margin-left:14px;background:var(--red);color:#fff;font-size:14px;padding:0 22px;height:26px;line-height:26px;min-width:100px;text-align:center}
  .features{display:flex;gap:22px;margin:14px 0 0 125px}
  .feature{display:flex;align-items:flex-start;gap:6px;font-size:8.5px;font-weight:600;line-height:1.25;width:100px}
  .feature__icon{width:15px;height:15px;flex:none;background:var(--icon);border-radius:2px;display:flex;align-items:center;justify-content:center}
  .product__body{display:flex;margin-top:14px}
  .figure{width:125px;flex:none;position:relative}
  .figure__ref{font-size:7.5px;color:var(--muted);display:block;margin:0 0 6px 16px}
  .figure__shape{margin-left:16px}
  .specs{width:345px;font-size:9px}
  .specs__row{display:flex;background:var(--row);border-bottom:2px solid #fff;min-height:21px;align-items:center}
  .specs__row:nth-child(even){background:var(--row-alt)}
  .specs__label{width:78px;padding-left:8px;color:var(--ink)}
  .specs__value{flex:1;padding:4px 8px;color:var(--muted);line-height:1.35}
</style>
</head>
<body>
<main class="spread">

  <section class="page page--left">
    <div class="banner" role="img" aria-label="Foto de teto iluminado com plafons LED"></div>
    <div class="side-band"><span>Luminárias LED &nbsp;|&nbsp; Catálogo 2018</span></div>

    <article class="product" style="top:140px">
      <header class="product__head">
        <h2 class="product__title">Luminária Plafon LED</h2>
        <span class="product__tag">Sobrepor</span>
      </header>
      <div class="features">
        <div class="feature"><span class="feature__icon"><svg width="9" height="9" viewBox="0 0 10 10"><path d="M2 5l2 2 4-4" stroke="#fff" stroke-width="1.6" fill="none"/></svg></span>Garantia<br>de 3 anos</div>
        <div class="feature"><span class="feature__icon"><svg width="9" height="9" viewBox="0 0 10 10"><path d="M5 1l3.5 1.5V5c0 2-1.6 3.4-3.5 4C3.1 8.4 1.5 7 1.5 5V2.5z" fill="#fff"/></svg></span>Índice de<br>Proteção IP 65</div>
        <div class="feature"><span class="feature__icon"><svg width="9" height="9" viewBox="0 0 10 10"><circle cx="5" cy="5" r="3.5" stroke="#fff" stroke-width="1.2" fill="none"/><path d="M5 3v2.2l1.4 1" stroke="#fff" stroke-width="1" fill="none"/></svg></span>Vida Útil de<br>25.000 horas</div>
      </div>
      <div class="product__body">
        <div class="figure">
          <span class="figure__ref">Ref. 001</span>
          <div class="figure__shape" role="img" aria-label="Foto do plafon LED de sobrepor quadrado" style="width:95px;height:95px;border-radius:10px;background:radial-gradient(circle at 45% 40%,#ffffff 0%,#f1f1f1 60%,#d6d6d6 100%);box-shadow:0 2px 5px rgba(0,0,0,.15)"></div>
        </div>
        <div class="specs">
          <div class="specs__row"><span class="specs__label">Potência</span><span class="specs__value">3w, 6w, 12w, 18w, 25w, 30w, 36w, 42w, 48w</span></div>
          <div class="specs__row"><span class="specs__label">Cor da Luz</span><span class="specs__value">Branco Quente, Branco Frio</span></div>
          <div class="specs__row"><span class="specs__label">Formato</span><span class="specs__value">Quadrado, Redondo, Retangular</span></div>
          <div class="specs__row"><span class="specs__label">Material</span><span class="specs__value">Acrílico e Alumínio</span></div>
          <div class="specs__row"><span class="specs__label">Voltagem</span><span class="specs__value">110v - 220v</span></div>
          <div class="specs__row"><span class="specs__label">Tamanho</span><span class="specs__value">8,5cm, 12cm, 17cm, 22,5cm, 30cm,<br>10x120cm, 30x60cm, 40cm, 60cm</span></div>
          <div class="specs__row"><span class="specs__label">Lúmens</span><span class="specs__value">180, 660, 1620, 1440, 2440, 3640</span></div>
        </div>
      </div>
    </article>

    <article class="product" style="top:470px">
      <header class="product__head">
        <h2 class="product__title">Luminária Plafon LED</h2>
        <span class="product__tag">Embutir</span>
      </header>
      <div class="features">
        <div class="feature"><span class="feature__icon"><svg width="9" height="9" viewBox="0 0 10 10"><path d="M2 5l2 2 4-4" stroke="#fff" stroke-width="1.6" fill="none"/></svg></span>Garantia<br>de 3 anos</div>
        <div class="feature"><span class="feature__icon"><svg width="9" height="9" viewBox="0 0 10 10"><path d="M5 1l3.5 1.5V5c0 2-1.6 3.4-3.5 4C3.1 8.4 1.5 7 1.5 5V2.5z" fill="#fff"/></svg></span>Índice de<br>Proteção IP 65</div>
        <div class="feature"><span class="feature__icon"><svg width="9" height="9" viewBox="0 0 10 10"><circle cx="5" cy="5" r="3.5" stroke="#fff" stroke-width="1.2" fill="none"/><path d="M5 3v2.2l1.4 1" stroke="#fff" stroke-width="1" fill="none"/></svg></span>Vida Útil de<br>25.000 horas</div>
      </div>
      <div class="product__body">
        <div class="figure">
          <span class="figure__ref">Ref. 002</span>
          <div class="figure__shape" role="img" aria-label="Foto do plafon LED de embutir redondo" style="width:95px;height:95px;border-radius:50%;background:radial-gradient(circle at 45% 40%,#ffffff 0%,#f1f1f1 60%,#cfcfcf 100%);box-shadow:0 2px 5px rgba(0,0,0,.15)"></div>
        </div>
        <div class="specs">
          <div class="specs__row"><span class="specs__label">Potência</span><span class="specs__value">3w, 6w, 12w, 18w, 25w, 30w, 36w, 40w, 41w,<br>42w, 48w</span></div>
          <div class="specs__row"><span class="specs__label">Cor da Luz</span><span class="specs__value">Branco Frio, Branco Morno, Branco Quente</span></div>
          <div class="specs__row"><span class="specs__label">Formato</span><span class="specs__value">Quadrado, Redondo</span></div>
          <div class="specs__row"><span class="specs__label">Material</span><span class="specs__value">Acrílico e Alumínio</span></div>
          <div class="specs__row"><span class="specs__label">Voltagem</span><span class="specs__value">110v - 220v</span></div>
          <div class="specs__row"><span class="specs__label">Tamanho</span><span class="specs__value">8,5cm, 12cm, 17cm, 22,5cm, 30cm,<br>30x60cm, 40cm, 60cm, 30x60cm</span></div>
          <div class="specs__row"><span class="specs__label">Lúmens</span><span class="specs__value">240, 660, 880, 1640, 2440, 3640</span></div>
        </div>
      </div>
    </article>

    <span class="page-number">05</span>
  </section>

  <section class="page page--right">
    <div class="banner" role="img" aria-label="Foto de ambiente interno com iluminação LED no teto"></div>
    <div class="spine-strip"></div>
    <div class="side-band"><span>Luminárias LED &nbsp;|&nbsp; Catálogo 2018</span></div>

    <article class="product" style="top:140px">
      <header class="product__head">
        <h2 class="product__title" style="margin-left:125px">Luminária LED</h2>
        <span class="product__tag" style="margin-left:40px">Pública</span>
      </header>
      <div class="features">
        <div class="feature"><span class="feature__icon"><svg width="9" height="9" viewBox="0 0 10 10"><path d="M2 5l2 2 4-4" stroke="#fff" stroke-width="1.6" fill="none"/></svg></span>Garantia<br>de 3 anos</div>
        <div class="feature"><span class="feature__icon"><svg width="9" height="9" viewBox="0 0 10 10"><path d="M5 1l3.5 1.5V5c0 2-1.6 3.4-3.5 4C3.1 8.4 1.5 7 1.5 5V2.5z" fill="#fff"/></svg></span>Índice de<br>Proteção IP 65</div>
        <div class="feature"><span class="feature__icon"><svg width="9" height="9" viewBox="0 0 10 10"><circle cx="5" cy="5" r="3.5" stroke="#fff" stroke-width="1.2" fill="none"/><path d="M5 3v2.2l1.4 1" stroke="#fff" stroke-width="1" fill="none"/></svg></span>Vida Útil de<br>25.000 horas</div>
      </div>
      <div class="product__body">
        <div class="figure">
          <span class="figure__ref">Ref. 003</span>
          <div class="figure__shape" role="img" aria-label="Foto da luminária LED pública para poste" style="width:62px;height:125px;margin-left:30px;border-radius:4px;background:linear-gradient(180deg,#3a3a3a 0%,#5a5a5a 55%,#2a2a2a 100%)"></div>
        </div>
        <div class="specs">
          <div class="specs__row"><span class="specs__label">Potência</span><span class="specs__value">30w, 50w, 100w, 150w, 24w, 20w, 50w, 100w</span></div>
          <div class="specs__row"><span class="specs__label">Cor da Luz</span><span class="specs__value">Branco Frio</span></div>
          <div class="specs__row"><span class="specs__label">Formato</span><span class="specs__value">Pétala, Micro LED</span></div>
          <div class="specs__row"><span class="specs__label">Material</span><span class="specs__value">Metal</span></div>
          <div class="specs__row"><span class="specs__label">Voltagem</span><span class="specs__value">110v - 220v</span></div>
          <div class="specs__row"><span class="specs__label">Tamanho</span><span class="specs__value">30x15cm, 40x21cm, 72x28cm, 95,5x35cm,<br>57x14cm, 53x23cm, 35x28cm</span></div>
        </div>
      </div>
    </article>

    <article class="product" style="top:470px">
      <header class="product__head">
        <h2 class="product__title" style="margin-left:125px">Luminária LED</h2>
        <span class="product__tag" style="margin-left:40px">Posto</span>
      </header>
      <div class="features">
        <div class="feature"><span class="feature__icon"><svg width="9" height="9" viewBox="0 0 10 10"><path d="M2 5l2 2 4-4" stroke="#fff" stroke-width="1.6" fill="none"/></svg></span>Garantia<br>de 1 ano</div>
        <div class="feature"><span class="feature__icon"><svg width="9" height="9" viewBox="0 0 10 10"><path d="M5 1l3.5 1.5V5c0 2-1.6 3.4-3.5 4C3.1 8.4 1.5 7 1.5 5V2.5z" fill="#fff"/></svg></span>Índice de<br>Proteção IP 65</div>
        <div class="feature"><span class="feature__icon"><svg width="9" height="9" viewBox="0 0 10 10"><circle cx="5" cy="5" r="3.5" stroke="#fff" stroke-width="1.2" fill="none"/><path d="M5 3v2.2l1.4 1" stroke="#fff" stroke-width="1" fill="none"/></svg></span>Vida Útil de<br>25.000 horas</div>
      </div>
      <div class="product__body">
        <div class="figure">
          <span class="figure__ref">Ref. 004</span>
          <div class="figure__shape" role="img" aria-label="Foto de luminárias LED para posto de combustível" style="width:95px;height:105px;background:linear-gradient(160deg,#d9dde2 0%,#b9bfc6 50%,#e6e8eb 100%)"></div>
        </div>
        <div class="specs">
          <div class="specs__row"><span class="specs__label">Potência</span><span class="specs__value">50w, 100w, 150w</span></div>
          <div class="specs__row"><span class="specs__label">Cor da Luz</span><span class="specs__value">Branco Frio - 6500k</span></div>
          <div class="specs__row"><span class="specs__label">Formato</span><span class="specs__value">Retangular, Quadrado</span></div>
          <div class="specs__row"><span class="specs__label">Material</span><span class="specs__value">Alumínio</span></div>
          <div class="specs__row"><span class="specs__label">Voltagem</span><span class="specs__value">110v - 220v</span></div>
          <div class="specs__row"><span class="specs__label">Tamanho</span><span class="specs__value">34 x 16 x 9cm, 380 x 327 x 61mm<br>500 x 440 x 180mm</span></div>
          <div class="specs__row"><span class="specs__label">Lúmens</span><span class="specs__value">5.000, 7.400, 12.000</span></div>
        </div>
      </div>
    </article>

    <span class="page-number">06</span>
  </section>

</main>
</body>
</html>
```